Custom workshop/manufacture for custom furniture, architectural millwork and kitchen cabinetry

simple and clean. I like this website:
http://www.velmarostudio.com

Attached are random ideas

Target Market(s)

residential, commercial, hospitality, interior designers, architects, contractors

Coding

Coded - Design and coding required

Number of Pages Required

5+ page

Font styles to use
Other font styles liked:
• Avenir next

Requirements
Must have
• drop down menu for work - residential - commercial

```html
<!DOCTYPE html>
<html lang="en">
<head>
<meta charset="utf-8">
<title>Company Name — Woodwork &amp; Interiors</title>
<link rel="stylesheet" href="https://fonts.googleapis.com/css2?family=Montserrat:wght@400;500;600;700&family=Mulish:wght@400;600;700&display=swap">
<style>
:root{
  --ink:#2b2b2b;
  --ink-soft:#555;
  --muted:#8a8a8a;
  --line:#e2e2e2;
  --paper:#ffffff;
  --band:#2f2f2f;
  --dark:#333333;
  --wood-1:#6b3a1c;
  --wood-2:#3a1f10;
}
*{box-sizing:border-box;margin:0;padding:0}
html,body{width:1200px;height:2711px;overflow:hidden}
body{position:relative;background:var(--paper);color:var(--ink);font-family:"Mulish",sans-serif;font-size:13.5px}
.abs{position:absolute}
h2,h3,.nav a,.btn{font-family:"Montserrat",sans-serif}

/* header */
.site-header{position:absolute;left:0;top:0;width:1200px;height:94px;background:var(--paper);border-bottom:1px solid var(--line)}
.brand{left:110px;top:30px;font-family:"Montserrat",sans-serif;font-weight:600;font-size:17px;color:var(--ink);display:flex;align-items:center;gap:8px}
.brand-mark{width:14px;height:14px;border:2px solid var(--ink)}
.topinfo{top:10px;font-size:12px;color:var(--ink-soft);display:flex;align-items:center;gap:8px;height:24px}
.topinfo svg{width:14px;height:14px}
.topinfo.sep{border-left:1px solid var(--line);padding-left:14px}
.nav{left:230px;top:58px;display:flex;gap:42px}
.nav a{font-size:12px;font-weight:600;color:var(--ink);text-decoration:none;text-transform:uppercase}
.social-top{right:80px;top:0;display:flex}
.social-top span{width:38px;height:38px;border-left:1px solid var(--line)}
.social-top span:last-child{border-right:1px solid var(--line)}
.call-btn{left:930px;top:54px;width:190px;height:26px;background:var(--dark);color:#fff;font-family:"Montserrat",sans-serif;font-weight:600;font-size:11.5px;display:flex;align-items:center;justify-content:center;gap:8px;clip-path:polygon(10px 0,100% 0,100% 100%,0 100%)}

/* hero */
.hero{left:0;top:94px;width:1200px;height:513px;background:linear-gradient(180deg,#7a4426 0%,var(--wood-1) 45%,var(--wood-2) 100%)}
.hero-title{left:141px;top:282px;color:#fff;font-family:"Montserrat",sans-serif;font-weight:700;font-size:42px;line-height:48px;letter-spacing:1px}
.hero-sub{left:141px;top:382px;color:#fff;font-family:"Montserrat",sans-serif;font-weight:600;font-size:19px;letter-spacing:3.5px}
.btn-light{left:141px;top:430px;width:117px;height:40px;background:#fff;color:var(--ink);font-size:12px;font-weight:700;display:flex;align-items:center;justify-content:center}
.hero-arrow{top:310px;width:52px;height:52px}
.quote{left:735px;top:155px;width:322px;height:393px;background:#fff;padding:26px 28px;box-shadow:0 4px 18px rgba(0,0,0,.25)}
.quote h3{text-align:center;font-size:20px;font-weight:600;letter-spacing:1px;margin-bottom:14px}
.field{height:40px;border:1px solid var(--line);margin-bottom:14px;padding:11px 12px;font-size:11.5px;color:#aaa}
.field.area{height:90px}
.btn-dark{height:42px;background:var(--dark);color:#fff;font-size:13px;font-weight:700;display:flex;align-items:center;justify-content:center;letter-spacing:.5px}

/* section heads */
.sec-head{font-size:27px;font-weight:600;letter-spacing:1px;color:var(--ink)}
.underline{height:3px;background:var(--ink);width:38px}
.underline::after{content:"";position:absolute;left:44px;top:0;width:8px;height:3px;background:var(--ink)}
.center{text-align:center;left:0;width:1200px}

/* about */
.about-photo{left:80px;top:687px;width:343px;height:473px;background:linear-gradient(90deg,#1f3563 0%,#2b4a85 30%,#e8ecef 55%,#cfd6dc 100%)}
.about-frame{left:125px;top:717px;width:327px;height:476px;border:9px solid var(--dark)}
.about-text{left:497px;top:788px;width:610px;font-size:13px;line-height:23.5px;color:var(--ink-soft)}
.about-text p+p{margin-top:23px}
.service{top:1026px;width:200px;text-align:center}
.diamond{width:48px;height:48px;margin:0 auto}
.service h4{margin-top:14px;font-family:"Montserrat",sans-serif;font-size:12.5px;font-weight:600;color:var(--ink)}
.service p{font-size:13px;line-height:23px;color:var(--ink-soft);margin-top:4px}

/* gallery */
.filters{left:405px;top:1334px;display:flex;gap:6px}
.filters span{height:36px;padding:0 13px;border:1px solid var(--line);display:flex;align-items:center;font-family:"Montserrat",sans-serif;font-size:11px;font-weight:600;color:var(--ink)}
.filters span.active{background:var(--dark);color:#fff;border-color:var(--dark)}
.tile{width:279px}

/* contact */
.contact-card{top:2118px;width:278px;height:224px;text-align:center;padding-top:26px}
.contact-card.raised{box-shadow:0 6px 24px rgba(0,0,0,.13)}
.icon-dot{width:40px;height:40px;border-radius:50%;background:#ececec;margin:0 auto;display:flex;align-items:center;justify-content:center}
.contact-card h4{font-family:"Montserrat",sans-serif;font-weight:600;font-size:18.5px;margin-top:20px}
.contact-card p{font-size:11.5px;line-height:17px;color:var(--ink-soft);margin-top:8px}
.contact-card strong{display:block;font-family:"Montserrat",sans-serif;font-size:16.5px;font-weight:600;margin-top:20px;line-height:22px}

/* newsletter & footer */
.newsletter{left:0;top:2403px;width:1200px;height:127px;background:var(--band);color:#fff}
.newsletter h3{position:absolute;left:168px;top:42px;font-size:25px;font-weight:600;letter-spacing:1px}
.nl-line{left:172px;top:86px;width:38px;height:3px;background:#fff}
.nl-field{left:408px;top:52px;width:384px;height:32px;border-bottom:1px solid #888;font-size:11.5px;color:#ddd;padding-top:4px}
.nl-btn{left:853px;top:44px;width:179px;height:42px;border:2px solid #fff;font-size:13px;font-weight:700;display:flex;align-items:center;justify-content:center;letter-spacing:.5px}
.social-foot{left:510px;top:2577px;display:flex}
.social-foot span{width:38px;height:36px;border:1px solid var(--line);margin-left:-1px}
.copyright{top:2644px;font-size:11.5px;color:var(--ink-soft)}
</style>
</head>
<body>

<header class="site-header">
  <div class="abs brand"><span class="brand-mark"></span>Company Name</div>
  <div class="abs topinfo" style="left:230px">
    <svg viewBox="0 0 16 16"><rect x="1" y="3" width="14" height="10" fill="#444"/><path d="M1 3l7 6 7-6" stroke="#fff" fill="none"/></svg>
    info@companyname.com
  </div>
  <div class="abs topinfo sep" style="left:408px">
    <svg viewBox="0 0 16 16"><circle cx="8" cy="8" r="6.5" fill="none" stroke="#444" stroke-width="2"/><path d="M8 4v4l3 2" stroke="#444" stroke-width="1.6" fill="none"/></svg>
    Mon - Fri at 8am to 5pm, Closed Sat and Sun
  </div>
  <div class="abs social-top"><span></span><span></span><span></span><span></span></div>
  <nav class="abs nav"><a>Home</a><a>About Us</a><a>Services</a><a>Gallery</a><a>Contact Us</a></nav>
  <div class="abs call-btn">
    <svg width="12" height="12" viewBox="0 0 16 16"><path d="M3 1l3 3-2 2c1 2 4 5 6 6l2-2 3 3-2 2C7 15 1 9 1 3z" fill="#fff"/></svg>
    CALL US: 123.456.7890
  </div>
</header>

<section class="abs hero" role="img" aria-label="Kitchen with warm wooden cabinetry and granite counters"></section>
<svg class="abs hero-arrow" style="left:14px" viewBox="0 0 52 52"><path d="M26 3L49 26 26 49 3 26z" fill="none" stroke="#fff" stroke-width="2.5"/><path d="M30 18l-8 8 8 8" fill="none" stroke="#fff" stroke-width="2.5"/></svg>
<svg class="abs hero-arrow" style="left:1134px" viewBox="0 0 52 52"><path d="M26 3L49 26 26 49 3 26z" fill="none" stroke="#fff" stroke-width="2.5"/><path d="M22 18l8 8-8 8" fill="none" stroke="#fff" stroke-width="2.5"/></svg>
<h1 class="abs hero-title">WOODWORK &amp;<br>INTERIORS</h1>
<div class="abs hero-sub">HANDCRAFTED IN BROOKLYN</div>
<div class="abs btn btn-light">MORE INFO</div>

<form class="abs quote">
  <h3>GET YOUR FREE QUOTE</h3>
  <div class="field">Your Name *</div>
  <div class="field">Your Email *</div>
  <div class="field">Your Phone *</div>
  <div class="field area">Message</div>
  <div class="btn btn-dark">SUBMIT NOW</div>
</form>

<!-- about -->
<div class="abs about-photo" role="img" aria-label="White built-in shelving unit with folded towels and baskets in a blue bathroom"></div>
<div class="abs about-frame"></div>
<h2 class="abs sec-head" style="left:497px;top:710px">WHO WE ARE</h2>
<div class="abs underline" style="left:497px;top:756px"></div>
<div class="abs about-text">
  <p>Lorem ipsum dolor sit amet, consectetur adipiscing elit. Nulla vehicula malesuada nisi eu rutrum. Maecenas purus diam, lobortis at velit eget, ultricies posuere augue. Nullam nec lectus a augue dictum euismod ut sed ex. Integer pretium arcu neque, vitae mollis massa consequat eu. In eget dolor luctus, varius dui fringilla, lobortis odio. Cras molestie nunc pretium, dictum lorem vel, vulputate mi. Etiam ac ligula bibendum, luctus diam sit amet, rutrum ipsum.</p>
  <p>Praesent tempus at neque non hendrerit. In euismod vestibulum sodales. Fusce feugiat dapibus facilisis. Sed interdum mauris sed vulputate fringilla. Sed purus dui, tempus tempor velit vel, feugiat eleifend nulla [...]</p>
</div>

<div class="abs service" style="left:496px">
  <svg class="diamond" viewBox="0 0 48 48"><path d="M24 3L45 24 24 45 3 24z" fill="none" stroke="#2b2b2b" stroke-width="3"/><rect x="16" y="15" width="16" height="18" fill="none" stroke="#2b2b2b" stroke-width="2"/><line x1="16" y1="21" x2="32" y2="21" stroke="#2b2b2b" stroke-width="2"/><rect x="19.5" y="24" width="9" height="6" fill="#2b2b2b"/></svg>
  <h4>KITCHEN REMODELS</h4>
  <p>Lorem ipsum dolor sit amet,<br>consectetur adipiscing</p>
</div>
<div class="abs service" style="left:711px">
  <svg class="diamond" viewBox="0 0 48 48"><path d="M24 3L45 24 24 45 3 24z" fill="none" stroke="#2b2b2b" stroke-width="3"/><path d="M14 24h20v3a6 6 0 0 1-6 6h-8a6 6 0 0 1-6-6z" fill="#2b2b2b"/><path d="M17 24v-8a3 3 0 0 1 6 0" fill="none" stroke="#2b2b2b" stroke-width="2"/></svg>
  <h4>BATHROOM REMODELS</h4>
  <p>Lorem ipsum dolor sit amet,<br>consectetur adipiscing</p>
</div>
<div class="abs service" style="left:923px">
  <svg class="diamond" viewBox="0 0 48 48"><path d="M24 3L45 24 24 45 3 24z" fill="none" stroke="#2b2b2b" stroke-width="3"/><path d="M24 14l10 9h-3v9h-5v-6h-4v6h-5v-9h-3z" fill="#2b2b2b"/></svg>
  <h4>EXISTING HOME</h4>
  <p>Lorem ipsum dolor sit amet,<br>consectetur adipiscing</p>
</div>

<!-- gallery -->
<h2 class="abs sec-head center" style="top:1245px">GALLERY</h2>
<div class="abs underline" style="left:574px;top:1292px"></div>
<div class="abs filters"><span class="active">ALL WORKS</span><span>KITCHEN</span><span>BATHROOM</span><span>OTHERS</span></div>

<div class="abs tile" style="left:155px;top:1417px;height:206px;background:linear-gradient(135deg,#e6e8e6,#b9bdb8 60%,#6e6a64)" role="img" aria-label="Bright white kitchen with island"></div>
<div class="abs tile" style="left:155px;top:1650px;height:314px;background:linear-gradient(160deg,#6f8a8f,#445b63 60%,#9aa6a6)" role="img" aria-label="Blue glass mosaic tile shower wall"></div>
<div class="abs tile" style="left:461px;top:1417px;height:314px;background:linear-gradient(180deg,#b9c3c2,#8f9998 55%,#e9ecec)" role="img" aria-label="Bathroom vanity with white cabinets and large mirror"></div>
<div class="abs tile" style="left:461px;top:1758px;height:206px;background:linear-gradient(180deg,#6a6660,#3b4b6e 60%,#5c4a3a)" role="img" aria-label="Bedroom with built-in bookshelves and blue bedding"></div>
<div class="abs tile" style="left:766px;top:1417px;height:206px;background:linear-gradient(90deg,#56606b,#8b8f94 50%,#b8b2a7)" role="img" aria-label="Hallway with built-in bookcase"></div>
<div class="abs tile" style="left:766px;top:1650px;height:314px;background:linear-gradient(90deg,#cfd3d3,#a9b0b1 60%,#213566)" role="img" aria-label="Glass walk-in shower with marble tile"></div>

<!-- contact -->
<h2 class="abs sec-head center" style="top:2019px">CONTACT US</h2>
<div class="abs underline" style="left:574px;top:2066px"></div>

<div class="abs contact-card" style="left:157px">
  <div class="icon-dot"><svg width="16" height="16" viewBox="0 0 16 16"><rect x="1" y="3" width="14" height="10" fill="#333"/><path d="M1 3l7 6 7-6" stroke="#ececec" fill="none"/></svg></div>
  <h4>SEND A MESSAGE</h4>
  <p>Tell us the reason for your query and<br>we'll give you an answer.</p>
  <strong>info@companyname.com</strong>
</div>
<div class="abs contact-card raised" style="left:461px">
  <div class="icon-dot"><svg width="16" height="16" viewBox="0 0 16 16"><path d="M3 1l3 3-2 2c1 2 4 5 6 6l2-2 3 3-2 2C7 15 1 9 1 3z" fill="#333"/></svg></div>
  <h4>MAKE A CALL</h4>
  <p>If you have any questions, just call us<br>and our manager will help you.</p>
  <strong>123.456.7890</strong>
</div>
<div class="abs contact-card" style="left:795px">
  <div class="icon-dot"><svg width="16" height="16" viewBox="0 0 16 16"><path d="M8 1a5 5 0 0 1 5 5c0 4-5 9-5 9S3 10 3 6a5 5 0 0 1 5-5z" fill="#333"/><circle cx="8" cy="6" r="2" fill="#ececec"/></svg></div>
  <h4>ADDRESS</h4>
  <p>Our office is open from 8am to 5pm<br>Monday through Friday.</p>
  <strong>123 Lorem Ipsum Dolor,<br>Sit 272 dolor, amet.</strong>
</div>

<!-- newsletter -->
<section class="abs newsletter">
  <h3>NEWSLETTER</h3>
  <div class="abs nl-line" style="left:172px;top:86px"></div>
  <div class="abs nl-field">Enter your email address</div>
  <div class="abs btn nl-btn">SUBSCRIBE</div>
</section>

<footer>
  <div class="abs social-foot"><span></span><span></span><span></span><span></span></div>
  <p class="abs copyright center">Company Name © 2018. All Rights Reserved</p>
</footer>

</body>
</html>
```